Family owned plumbing contractor needs eye catching business card design

Business cards that are unique, eye catching, and provide customers with general company information, such as name, address, phone number, website, employee name/title, cell phone #, & email address. We are transitioning to a new logo that utilizes a more retro feel, so we are interested in seeing some cool old school designs in the mix. We are liking the dark background on some of the samples on this website. If that is workable with our artwork, we would like to see that incorporated into the design.
Contact Information for Business Card
Copperline Pipeworks, Inc.
www.copperlinepipeworks.example
(555) 392-7068 phone
Nevada License #64205
California License #5810473
Dale Wrennick, President
(555) 618-9032 cell
dale@copperlinepipeworks.example
Residential * Commercial * Service
Requirements
Must have
- The business card details listed above & logo provided.
Nice to have
- I made some notes about color options in the description.

```html
<!DOCTYPE html>
<html lang="en">
<head>
<meta charset="utf-8">
<title>Copperline Pipeworks, Inc. – Business Card</title>
<link rel="stylesheet" href="https://fonts.googleapis.com/css2?family=Arimo:wght@400;700&display=swap">
<style>
  :root {
    --backdrop: #2b2b2d;
    --slate: #5b7d98;
    --slate-dark: #3f5d78;
    --teal: #6fc3b0;
    --paper: #ffffff;
    --ink-light: #ffffff;
  }
  * { box-sizing: border-box; margin: 0; padding: 0; }
  html, body { width: 1200px; height: 880px; overflow: hidden; }
  body {
    background: var(--backdrop);
    font-family: "Arimo", Arial, sans-serif;
    position: relative;
  }
  .card {
    position: absolute;
    left: 267px;
    width: 665px;
    height: 380px;
    border-radius: 26px;
    overflow: hidden;
  }
  .card--front { top: 40px; background: var(--slate); }
  .card--back { top: 460px; background: var(--paper); }

  .brand {
    position: absolute;
    display: flex;
    align-items: center;
    gap: 14px;
    font-weight: 700;
    font-size: 22px;
    line-height: 1.2;
  }
  .brand__dot {
    width: 26px; height: 26px;
    border-radius: 50%;
    background: var(--teal);
    flex: none;
  }
  .card--front .brand {
    left: 0; right: 0; top: 140px;
    justify-content: center;
    color: var(--ink-light);
  }
  .card--back .brand {
    left: 30px; top: 170px;
    width: 240px;
    color: var(--slate-dark);
    font-size: 20px;
  }

  .services {
    position: absolute;
    left: 0; right: 0; bottom: 52px;
    text-align: center;
    color: var(--ink-light);
    font-size: 17px;
    font-weight: 700;
    letter-spacing: 3px;
  }
  .services .sep { margin: 0 10px; }

  .details {
    position: absolute;
    top: 0; right: 0; bottom: 0;
    width: 385px;
    background: var(--slate);
    color: var(--ink-light);
    padding: 42px 30px 0 36px;
  }
  .details__company {
    font-size: 25px;
    font-weight: 700;
    line-height: 1.08;
    text-transform: uppercase;
  }
  .details__name {
    margin-top: 16px;
    font-size: 22px;
    font-weight: 700;
    line-height: 1;
  }
  .details__title { font-size: 15px; margin-bottom: 20px; }
  .details__line { font-size: 15px; line-height: 1.3; }
  .details__line b { font-weight: 700; }
  .details__gap { margin-top: 12px; }
  .details__web {
    margin-top: 16px;
    font-size: 15px;
    font-weight: 700;
  }
</style>
</head>
<body>
  <section class="card card--front" aria-label="Business card front">
    <div class="brand"><span class="brand__dot"></span><span>Copperline Pipeworks, Inc.</span></div>
    <p class="services">✱ Residential <span class="sep">✱</span>Commercial<span class="sep">✱</span>Service</p>
  </section>

  <section class="card card--back" aria-label="Business card back">
    <div class="brand"><span class="brand__dot"></span><span>Copperline Pipeworks, Inc.</span></div>
    <div class="details">
      <h1 class="details__company">Copperline<br>Pipeworks, Inc.</h1>
      <p class="details__name">Dale Wrennick</p>
      <p class="details__title">President</p>
      <p class="details__line"><b>Cell:</b> (555) 618-9032</p>
      <p class="details__line">dale@copperlinepipeworks.example</p>
      <p class="details__line details__gap"><b>Phone:</b>(555) 392-7068</p>
      <p class="details__line">Nevada License #64205</p>
      <p class="details__line">California License #5810473</p>
      <p class="details__web">www.copperlinepipeworks.example</p>
    </div>
  </section>
</body>
</html>
```